Design a Professional Business Card for Velmora Arcs

Design a business card for Velmora Arcs, we are a National Sport Court Company.

West Region Address: 4175 Quill Harbor Ln, Suite #215 Fernhollow, Calvista 80467
East Region Address: 3817 Tamsin Rd E, Marlow Bay, Solvane 34583

Target Market(s)

High End Residential & Institutional Clients

Industry/Entity Type

Design & Construction

Contact Information for Business Card

Logo/Brand/Colors/ name, number (provided in comments)

Requirements
Must have
• Colors only provided in logo
Should not have
• Any other colors not in existing logo (attached)

```html
<!DOCTYPE html>
<html lang="en">
<head>
<meta charset="UTF-8">
<title>Velmora Arcs — Business Card</title>
<link href="https://fonts.googleapis.com/css2?family=Lato:wght@400;700;900&display=swap" rel="stylesheet">
<style>
  :root {
    --stage: #2e2e2e;
    --card-light: #f1f1f0;
    --card-dark: #121212;
    --brand-blue: #1f4a8a;
    --name-blue: #1b5584;
    --brand-green: #1e7a3c;
    --ink: #2a2a2a;
    --paper-text: #f2f2f2;
    --divider: #6a6a6a;
  }
  * { box-sizing: border-box; margin: 0; padding: 0; }
  html, body { width: 1200px; height: 800px; overflow: hidden; }
  body {
    background: var(--stage);
    font-family: "Lato", sans-serif;
    position: relative;
  }
  .card {
    position: absolute;
    width: 500px;
    height: 286px;
    border-radius: 14px;
    overflow: hidden;
  }
  .card--front { left: 70px; top: 257px; background: var(--card-light); color: var(--ink); }
  .card--back { left: 630px; top: 257px; background: var(--card-dark); color: var(--paper-text); }

  .brand { display: flex; align-items: center; gap: 10px; }
  .brand__dot { width: 34px; height: 34px; border-radius: 50%; background: var(--brand-blue); flex: none; }
  .brand__name { font-weight: 900; font-size: 26px; letter-spacing: 1px; text-transform: uppercase; color: var(--brand-blue); line-height: 1; }

  .holder { position: absolute; left: 34px; top: 40px; }
  .holder__name { font-weight: 700; font-size: 22px; color: var(--name-blue); letter-spacing: -0.2px; }
  .holder__title { font-size: 15px; margin-top: 4px; color: var(--ink); }
  .card--front .brand { position: absolute; right: 30px; top: 120px; }
  .contacts { position: absolute; left: 34px; bottom: 30px; list-style: none; }
  .contacts li { display: flex; align-items: center; gap: 10px; font-size: 14px; line-height: 22px; }
  .contacts svg { width: 14px; height: 14px; fill: var(--brand-green); flex: none; }

  .card--back .brand { position: absolute; left: 50%; top: 52px; transform: translateX(-50%); }
  .card--back .brand__dot { width: 44px; height: 44px; }
  .card--back .brand__name { font-size: 32px; }
  .divider { position: absolute; left: 250px; top: 140px; height: 110px; border-left: 1px dotted var(--divider); }
  .region { position: absolute; font-size: 13.5px; line-height: 19px; }
  .region--west { left: 30px; top: 170px; }
  .region--east { left: 272px; top: 150px; }
  .region__label { display: flex; align-items: center; gap: 7px; font-weight: 700; font-size: 15px; margin-bottom: 8px; }
  .region__label svg { width: 12px; height: 16px; }
  .region--west .region__label svg { fill: var(--brand-green); }
  .region--east .region__label svg { fill: var(--brand-blue); }
</style>
</head>
<body>
  <svg width="0" height="0" style="position:absolute">
    <symbol id="icon-pin" viewBox="0 0 12 16"><path d="M6 0a6 6 0 0 0-6 6c0 4.5 6 10 6 10s6-5.5 6-10a6 6 0 0 0-6-6zm0 8.5A2.5 2.5 0 1 1 6 3.5a2.5 2.5 0 0 1 0 5z"/></symbol>
  </svg>

  <section class="card card--front" aria-label="Card front">
    <div class="holder">
      <h1 class="holder__name">DORIAN L. HASKETT, MDLA</h1>
      <p class="holder__title">CEO &amp; Founder</p>
    </div>
    <div class="brand">
      <span class="brand__dot"></span>
      <span class="brand__name">Velmora Arcs</span>
    </div>
    <ul class="contacts">
      <li><svg viewBox="0 0 16 16"><path d="M3 2h3l1.5 3.5-2 1.2a8 8 0 0 0 3.8 3.8l1.2-2L14 10v3a1 1 0 0 1-1 1A11 11 0 0 1 2 3a1 1 0 0 1 1-1z"/></svg>(555) 555-0147</li>
      <li><svg viewBox="0 0 16 16"><path d="M5 1h6a1 1 0 0 1 1 1v12a1 1 0 0 1-1 1H5a1 1 0 0 1-1-1V2a1 1 0 0 1 1-1zm1 2v9h4V3z"/></svg>1-800-555-0192</li>
      <li><svg viewBox="0 0 16 16"><path d="M15 1 1 7l5 2 2 6z"/></svg>dorian@velmoraco.com</li>
      <li><svg viewBox="0 0 16 16"><path d="M8 1a7 7 0 1 0 0 14A7 7 0 0 0 8 1zm0 1.5c.8 0 1.8 1.7 2 4.5H6c.2-2.8 1.2-4.5 2-4.5zM2.6 7h2c.1-1.7.5-3.2 1-4.1A5.6 5.6 0 0 0 2.6 7zm8.8 0h2a5.6 5.6 0 0 0-3-4.1c.5.9.9 2.4 1 4.1zM2.6 9a5.6 5.6 0 0 0 3 4.1c-.5-.9-.9-2.4-1-4.1zm3.4 0c.2 2.8 1.2 4.5 2 4.5s1.8-1.7 2-4.5zm5.4 0c-.1 1.7-.5 3.2-1 4.1a5.6 5.6 0 0 0 3-4.1z"/></svg>www.velmoraarcs.com</li>
    </ul>
  </section>

  <section class="card card--back" aria-label="Card back">
    <div class="brand">
      <span class="brand__dot"></span>
      <span class="brand__name">Velmora Arcs</span>
    </div>
    <div class="divider"></div>
    <div class="region region--west">
      <p class="region__label"><svg><use href="#icon-pin"/></svg>West Region :</p>
      <p>4175 Quill Harbor Ln,<br>Suite #215 Fernhollow, Calvista<br>80467</p>
    </div>
    <div class="region region--east">
      <p class="region__label"><svg><use href="#icon-pin"/></svg>East Region :</p>
      <p>3817 Tamsin Rd E, Marlow Bay,<br>Solvane 34583</p>
    </div>
  </section>
</body>
</html>
```